Veltrop Partners Website - developing a website for a new IIoT (Industrial Internet of Things) startup

Hi All-

Thought I'd re-write this bit...

Firstly, to everyone who has submitted designs, thank you.

Basically, we are looking for a simple/ elegant / modern website with clean lines and design. Because this is a startup, we don't have a great deal of content. Therefore, I'm relying on the site to give us an established / international feel (no images of London, London attractions, or the London skyline please!) We will have offices in London / LA and Tokyo by the end of this year.

Selecting great images is really important. As I say, abstract is fine (less literal.) Black and white is fine as well. We need to convey our expertise to new, international clients, so this is v.important.

http://www.brevanti41.it/ (favourite)
http://www.crafthollowstudio.com/cases/

In terms of colour, I think white /grey/ black and maybe experiment with red for the word Veltrop and (possibly) Group. Please note** I need the following words / strap line written underneath the main logo: IIoT Strategy. Sensor Innovation. Machine Learning.

Whomever we chose to work with, this will be an ongoing partnership: we will continually need to add new content and update the site.

Thank you!

Dell.
Updates

**Please view updated brief description.

Target Market(s)

Mid-sized (£25M- £500M GBP) companies in the UK/ US and Asia. Facilities/ Construction/ Automotive/ Manufacturing / Engineering

Industry/Entity Type

Information Technology

Logo Text

Veltrop Partners -- IIoT Strategy. Sensor Innovation. Machine Learning (written underneath)

Coding

Coded - Design and coding required

Number of Pages Required

5+ page

Font styles to use
Sans Serif

Requirements
Must have
• An international, established, aspirational feel. Beautiful imagery. elegant infographics (nothing complex). CTA on homepage.
Should not have
• Anything cartoony / informal or naff corporate imagery.

```html
<!DOCTYPE html>
<html lang="en">
<head>
<meta charset="utf-8">
<title>Veltrop Partners in London</title>
<link href="https://fonts.googleapis.com/css2?family=Raleway:wght@400;600;700;800&family=Open+Sans:ital,wght@0,400;0,600;1,400&display=swap" rel="stylesheet">
<style>
:root{
  --red:#d8262c;
  --ink:#2b2b2b;
  --text:#555;
  --muted:#777;
  --white:#fff;
  --card:#f1f1f1;
  --band:#ececec;
  --footer:#3b3b3b;
  --footer-base:#2c2c2c;
  --footer-text:#bdbdbd;
}
*{margin:0;padding:0;box-sizing:border-box}
html,body{width:1200px;height:3482px;overflow:hidden}
body{font-family:"Open Sans",Arial,sans-serif;color:var(--text);background:var(--white);position:relative}
h1,h2,h3,h4,.brand,.nav{font-family:"Raleway",Arial,sans-serif}

/* header */
.site-header{position:absolute;top:0;left:0;width:1200px;height:81px;background:var(--white)}
.brand{position:absolute;left:100px;top:12px}
.brand-name{color:var(--red);font-weight:700;font-size:34px;line-height:36px;letter-spacing:.5px}
.brand-sub{color:var(--ink);font-weight:600;font-size:9px;letter-spacing:0;margin-top:4px;white-space:nowrap}
.nav{position:absolute;top:34px;left:0;width:1200px;height:14px}
.nav a{position:absolute;font-size:12px;font-weight:600;color:var(--ink);text-decoration:none;letter-spacing:.5px;transform:translateX(-50%)}

/* hero */
.hero{position:absolute;top:81px;left:0;width:1200px;height:499px;background:linear-gradient(180deg,#bcd1e6 0%,#9fb3c6 30%,#5b6570 60%,#3a3f45 100%)}
.hero-caption{position:absolute;left:100px;top:360px;width:492px;height:100px;background:rgba(0,0,0,.55);border-left:6px solid var(--red);padding:20px 0 0 26px;color:var(--white)}
.hero-caption h1{font-size:24px;font-weight:700;letter-spacing:.5px}
.hero-caption p{font-family:"Raleway",sans-serif;font-size:18px;margin-top:4px;letter-spacing:.3px}
.hero-dots{position:absolute;left:576px;top:479px;display:flex;gap:8px}
.hero-dots span{width:8px;height:8px;border-radius:50%;background:rgba(255,255,255,.6)}
.hero-dots span.on{background:var(--white)}

/* welcome */
.section-title{position:absolute;left:0;width:1200px;text-align:center;font-family:"Raleway",sans-serif;color:var(--ink)}
.welcome-title{top:652px;font-size:32px;font-weight:400}
.welcome-title b{font-weight:800}
.lead{position:absolute;left:190px;width:820px;text-align:center;font-size:12px;line-height:26px;color:var(--text)}
.heading-caps{font-size:24px;font-weight:700;letter-spacing:.5px}

/* service cards */
.card{position:absolute;top:984px;width:325px;height:474px;background:var(--card)}
.card-image{width:325px;height:253px}
.card-plus{position:absolute;left:139px;top:230px;width:46px;height:46px;border-radius:50%;background:var(--red);border:3px solid var(--white)}
.card h3{position:absolute;top:300px;width:100%;text-align:center;font-size:18px;font-weight:700;color:var(--ink)}
.card p{position:absolute;top:338px;left:36px;width:253px;text-align:center;font-size:12px;line-height:25px;color:var(--text)}

/* about */
.about{position:absolute;top:1546px;left:0;width:1200px;height:504px;background:linear-gradient(90deg,#6f7b88 0%,#a9b4bf 35%,#e8edf2 60%,#f6f8fa 100%)}
.about-copy{position:absolute;right:104px;top:72px;width:500px;text-align:right}
.about-copy h2{font-family:"Raleway",sans-serif;color:var(--ink);font-size:30px;font-weight:400;line-height:36px}
.about-copy h2 strong{display:block;font-weight:700;font-size:30px}
.about-copy p{font-size:13px;line-height:28px;color:var(--text);margin-top:18px}
.about-copy p+p{margin-top:10px}
.btn{position:absolute;right:0;top:308px;width:141px;height:41px;background:var(--red);color:var(--white);font-size:13px;font-weight:600;display:flex;align-items:center;justify-content:center}

/* team */
.member{position:absolute;top:2202px;width:168px;text-align:center}
.member-photo{width:168px;height:168px;border-radius:50%;background:radial-gradient(circle at 50% 45%,#e7e3df 0%,#cfd3d8 70%,#bfc4ca 100%)}
.member h4{font-size:17px;font-weight:700;color:var(--ink);margin-top:24px}
.member span{display:block;font-size:12px;color:var(--muted);margin-top:8px}
.team-arrow{position:absolute;top:2272px}

/* blog */
.blog{position:absolute;top:2516px;left:0;width:1200px;height:641px;background:var(--band)}
.post{position:absolute;top:132px;width:309px}
.post-image{width:309px;height:221px}
.post h3{font-family:"Raleway",sans-serif;font-size:17px;font-weight:600;line-height:30px;color:var(--ink);margin-top:30px}
.post time{display:block;font-size:12px;font-style:italic;color:var(--text);margin-top:6px}
.post p{font-size:13px;line-height:25px;color:var(--text);margin-top:10px}

/* footer */
.site-footer{position:absolute;top:3157px;left:0;width:1200px;height:273px;background:var(--footer);color:var(--footer-text);font-size:11px}
.site-footer h4{font-size:12px;font-weight:700;color:var(--white);letter-spacing:.5px}
.f-col{position:absolute;top:46px}
.f-col ul{list-style:none;margin-top:16px}
.f-col li{line-height:28px}
.f-about p{line-height:22px;margin-top:16px;width:330px}
.f-more{display:flex;align-items:center;gap:8px;color:var(--white);margin-top:12px;font-weight:600}
.f-contact li{display:flex;align-items:center;gap:8px}
.socials{display:flex;gap:8px;margin-top:12px}
.socials span{width:22px;height:22px;border-radius:50%;background:#8d8d8d}
.footer-base{position:absolute;top:3430px;left:0;width:1200px;height:52px;background:var(--footer-base);color:#9a9a9a;font-size:11px;text-align:center;line-height:52px}
</style>
</head>
<body>

<header class="site-header">
  <div class="brand">
    <div class="brand-name">VELTROP</div>
    <div class="brand-sub">IIoT Strategy. Sensor Innovation. Machine Learning.</div>
  </div>
  <nav class="nav">
    <a style="left:380px">HOME</a>
    <a style="left:469px">ABOUT</a>
    <a style="left:571px">STRATEGY</a>
    <a style="left:680px">SENSORS</a>
    <a style="left:787px">DATA &amp; AI</a>
    <a style="left:887px">EVENTS</a>
    <a style="left:977px">BLOG</a>
    <a style="left:1072px">CONTACT</a>
  </nav>
</header>

<section class="hero" role="img" aria-label="Wide photograph of a city skyline of glass office towers under a pale sky">
  <div class="hero-caption">
    <h1>VELTROP PARTNERS IN LONDON</h1>
    <p>OUR SERVICES ARE STRATEGY, SENSORS AND AI</p>
  </div>
  <div class="hero-dots"><span class="on"></span><span></span><span></span><span></span></div>
</section>

<h2 class="section-title welcome-title">Welcome to <b>VELTROP</b> partners</h2>
<p class="lead" style="top:710px">The core team at Veltrop Partners are Innovators, Engineers, PhDs and Data Scientists who assist mid-sized companies ($25M- $500M) to capitalise on the enormous potential of the Industrial Internet of Things ("IIoT.")</p>
<p class="lead" style="top:786px">Our three business units – Strategy, Sensors and AI – mean that we can provide expert advice to both new entrants and companies already familiar with IIoT.</p>

<h2 class="section-title heading-caps" style="top:907px">WHAT WE DO</h2>

<article class="card" style="left:100px">
  <div class="card-image" role="img" aria-label="Photo of hands reviewing charts on a tablet at a desk" style="background:linear-gradient(135deg,#e9edf2,#aab6c6 60%,#6d7b90)"></div>
  <div class="card-plus"><svg width="40" height="40" viewBox="0 0 40 40"><path d="M20 13v14M13 20h14" stroke="#fff" stroke-width="2"/></svg></div>
  <h3>STRATEGY</h3>
  <p>Our three business units – Strategy, Sensors and AI – mean that we can provide expert advice to both new entrants and companies already familiar with IIoT.</p>
</article>
<article class="card" style="left:439px">
  <div class="card-image" role="img" aria-label="Photo of a business meeting in a modern office" style="background:linear-gradient(135deg,#3c4450,#8792a0 55%,#c9cfd6)"></div>
  <div class="card-plus"><svg width="40" height="40" viewBox="0 0 40 40"><path d="M20 13v14M13 20h14" stroke="#fff" stroke-width="2"/></svg></div>
  <h3>SENSORS</h3>
  <p>The Sensor team are focused on innovation using Sensors and MEMS (Micro Electromechanical Systems.) We view ourselves as the conduit</p>
</article>
<article class="card" style="left:778px">
  <div class="card-image" role="img" aria-label="Photo from above of a team joining puzzle pieces on a table" style="background:linear-gradient(135deg,#2d3a5a,#4b5a7c 55%,#3a5b4a)"></div>
  <div class="card-plus"><svg width="40" height="40" viewBox="0 0 40 40"><path d="M20 13v14M13 20h14" stroke="#fff" stroke-width="2"/></svg></div>
  <h3>DATA &amp; AI</h3>
  <p>The Data &amp;amp; AI team focus on getting the maximum value from our customer's sensors. We are a small team of engineers and data scientists</p>
</article>

<section class="about" role="img" aria-label="Photo of a smiling businessman giving a thumbs up in a bright office">
  <div class="about-copy">
    <h2>ABOUT<strong>VELTROP PARTNERS IN LONDON</strong></h2>
    <p>The core team at Veltrop Partners are Innovators, Engineers, PhDs and Data Scientists who assist mid-sized companies ($25M- $500M) to capitalise on the enormous potential of the Industrial Internet of Things ("IIoT.")</p>
    <p>Our three business units – Strategy, Sensors and AI – mean that we can provide expert advice to both new entrants and companies already amiliar with IIoT.</p>
    <div class="btn">Read more info</div>
  </div>
</section>

<h2 class="section-title heading-caps" style="top:2118px">OUR TEAM</h2>
<svg class="team-arrow" style="left:103px" width="16" height="28" viewBox="0 0 16 28"><path d="M13 2L3 14l10 12" fill="none" stroke="#aaa" stroke-width="2"/></svg>
<svg class="team-arrow" style="left:1081px" width="16" height="28" viewBox="0 0 16 28"><path d="M3 2l10 12L3 26" fill="none" stroke="#aaa" stroke-width="2"/></svg>
<div class="member" style="left:164px"><div class="member-photo" role="img" aria-label="Portrait of team member"></div><h4>Arlen Voss</h4><span>Organisor</span></div>
<div class="member" style="left:399px"><div class="member-photo" role="img" aria-label="Portrait of team member"></div><h4>Arlen Voss</h4><span>Manager</span></div>
<div class="member" style="left:633px"><div class="member-photo" role="img" aria-label="Portrait of team member"></div><h4>Arlen Voss</h4><span>Accountant</span></div>
<div class="member" style="left:868px"><div class="member-photo" role="img" aria-label="Portrait of team member"></div><h4>Arlen Voss</h4><span>Researcher</span></div>

<section class="blog">
  <h2 class="section-title heading-caps" style="top:54px">BLOG POSTS</h2>
  <article class="post" style="left:100px">
    <div class="post-image" role="img" aria-label="Photo of a hand signing a document beside a phone and glasses" style="background:linear-gradient(135deg,#cfe0d4,#7f9c8a 60%,#4a5d52)"></div>
    <h3>Lorem Ipsum is simply dummy text<br>of the printing</h3>
    <time>Published March 31, 2016</time>
    <p>Lorem Ipsum is simply dummy text of the printing and typesetting industry. Lorem Ipsum has been the industry's standard dummy text ever since the 1500s...</p>
  </article>
  <article class="post" style="left:446px">
    <div class="post-image" role="img" aria-label="Photo of colleagues talking around an office table" style="background:linear-gradient(135deg,#d9dde4,#8f97a6 55%,#4e5563)"></div>
    <h3>Lorem Ipsum is simply dummy text<br>of the printing</h3>
    <time>Published March 31, 2016</time>
    <p>Lorem Ipsum is simply dummy text of the printing and typesetting industry. Lorem Ipsum has been the industry's standard dummy text ever since the 1500s...</p>
  </article>
  <article class="post" style="left:794px">
    <div class="post-image" role="img" aria-label="Photo of a presenter at a board covered in notes before a seated team" style="background:linear-gradient(135deg,#e6e8ea,#a3a9b0 55%,#52575e)"></div>
    <h3>Lorem Ipsum is simply dummy text<br>of the printing</h3>
    <time>Published March 31, 2016</time>
    <p>Lorem Ipsum is simply dummy text of the printing and typesetting industry. Lorem Ipsum has been the industry's standard dummy text ever since the 1500s...</p>
  </article>
</section>

<footer class="site-footer">
  <div class="f-col f-about" style="left:104px">
    <h4>WHO WE ARE?</h4>
    <p>Lorem Ipsum is simply dummy text of the printing and typesetting industry. Lorem Ipsum has been the industry's standard dummy text ever since the 1500s, when an unknown printer took a galley of type and scrambled...</p>
    <div class="f-more">Read more info <svg width="12" height="12" viewBox="0 0 12 12"><circle cx="6" cy="6" r="6" fill="#fff"/><path d="M5 3.5L7.5 6 5 8.5" fill="none" stroke="#3b3b3b" stroke-width="1.5"/></svg></div>
  </div>
  <div class="f-col" style="left:529px">
    <h4>WELCOME</h4>
    <ul><li>About</li><li>Strategy</li><li>Sensors</li><li>Data &amp; AI</li><li>Events</li><li>Blog</li></ul>
  </div>
  <div class="f-col" style="left:708px">
    <h4>INFORMATION</h4>
    <ul><li>Terms &amp; Conditions</li><li>Privacy policy</li><li>Disclaimer</li><li>Contact us</li><li>Sitemap</li></ul>
  </div>
  <div class="f-col f-contact" style="left:907px">
    <h4>CONTACT INFO</h4>
    <ul>
      <li style="line-height:22px">120 Street name, City name,<br>Country name - 3652255</li>
      <li><svg width="12" height="12" viewBox="0 0 12 12"><path d="M2 1h3l1 3-1.5 1a7 7 0 003 3L9 6.5l3 1v3a1 1 0 01-1 1A10 10 0 011 2a1 1 0 011-1z" fill="#bdbdbd"/></svg>(+44) 555 - 0142</li>
      <li><svg width="12" height="10" viewBox="0 0 12 10"><rect x="0.5" y="0.5" width="11" height="9" fill="none" stroke="#bdbdbd"/><path d="M0.5 0.5L6 5.5l5.5-5" fill="none" stroke="#bdbdbd"/></svg>info@veltrop.com</li>
    </ul>
    <div class="socials"><span></span><span></span><span></span><span></span><span></span></div>
  </div>
</footer>
<div class="footer-base">© 2017. Veltrop. All rights reserved</div>

</body>
</html>
```